Defense contractor needs a roll-up for an exhibition

The booth we have booked has only a size of 3m².
So this will be the centerpiece of the whole booth.
We need a roll-up that attracts visitors and at the same time it should contain already designed graphics. These graphics are giving visitors an overview of our system. So it is necessary to have them exposed in a height that the booth personal can conveniently point with its fingers at them.
For information about our company and product visit:
https://www.brightlanternoptics.com/
For designing you should use Adobe Illustrator and the templates provided in the zip file, to guarantee a perfect print.
I have supplied my business card that you can copy the logo. As the company logo will be already at the booth nearby the top of the roll-up, you should not place it there. It can be in the middle or at the bottom.
I have uploaded a picture of the booth. The roll up will be placed at the left of the screen and has a size of 80cm x 200cm

Defense

Defense

Serif

Colors
0054AA
0677BA
7BADD7
CADEEF
E8F1F8

• you must use the Adobe Illustrator template to have a good printing result
• company logo on the upper side of the roll-up

```html
<!DOCTYPE html>
<html lang="en">
<head>
<meta charset="utf-8">
<title>Roll-up – Combat Training Systems</title>
<link rel="stylesheet" href="https://fonts.googleapis.com/css2?family=Bebas+Neue&family=Open+Sans:wght@700&display=swap">
<style>
  :root {
    --stage: #d9d9dc;
    --navy: #1b2473;
    --royal: #2f3f9e;
    --violet: #6a5aa8;
    --blush: #c88aa6;
    --ink: #06070d;
    --panel: #e4e6f4;
    --panel-shade: #b9bdd6;
    --panel-frame: #9aa0c4;
    --white: #ffffff;
    --rule: rgba(255,255,255,0.55);
  }
  * { box-sizing: border-box; margin: 0; padding: 0; }
  html, body { width: 1200px; height: 900px; overflow: hidden; }
  body { background: var(--stage); position: relative; }

  .rollup {
    position: absolute; left: 414px; top: 20px;
    width: 371px; height: 860px;
    display: flex; flex-direction: column;
    box-shadow: 0 6px 24px rgba(0,0,0,0.18);
  }

  .rollup-header {
    height: 101px; flex: none;
    background:
      radial-gradient(ellipse at 55% 40%, var(--violet) 0%, transparent 60%),
      linear-gradient(90deg, var(--navy) 0%, var(--royal) 50%, var(--navy) 100%);
    display: flex; align-items: center; justify-content: center;
  }
  .rollup-title {
    font-family: "Bebas Neue", sans-serif;
    color: var(--white);
    font-size: 28px; line-height: 1.0; letter-spacing: 0.2px;
    text-align: center; font-weight: 400;
  }

  .illustration {
    flex: none; position: relative;
    background: var(--panel);
  }
  .illustration::after {
    content: ""; position: absolute; inset: 14px 18px;
    border: 1.5px dashed var(--panel-frame); border-radius: 4px;
  }
  .illustration--field {
    height: 199px;
    background:
      radial-gradient(ellipse 45% 35% at 62% 68%, var(--panel-shade) 0%, transparent 100%),
      radial-gradient(ellipse 25% 18% at 26% 42%, var(--panel-shade) 0%, transparent 100%),
      radial-gradient(ellipse 30% 12% at 60% 18%, #cdd0e3 0%, transparent 100%),
      var(--panel);
  }
  .illustration--classroom {
    height: 190px;
    background:
      radial-gradient(ellipse 50% 40% at 48% 62%, var(--panel-shade) 0%, transparent 100%),
      radial-gradient(ellipse 22% 16% at 68% 34%, #9da79a 0%, transparent 100%),
      var(--panel);
  }

  .feature-band {
    height: 163px; flex: none;
    background:
      radial-gradient(ellipse at 85% 95%, var(--blush) 0%, transparent 45%),
      radial-gradient(ellipse at 50% 20%, var(--violet) 0%, transparent 55%),
      linear-gradient(90deg, var(--navy) 0%, var(--royal) 55%, var(--navy) 100%);
    padding: 12px 20px;
  }
  .feature-grid {
    display: grid; grid-template-columns: repeat(4, 1fr); grid-template-rows: 1fr 1fr;
    height: 100%;
  }
  .feature {
    display: flex; flex-direction: column; align-items: center; justify-content: flex-end;
    padding-bottom: 6px; gap: 5px;
  }
  .feature:not(:nth-child(4n+1)) { border-left: 1px solid var(--rule); }
  .feature:nth-child(-n+4) { border-bottom: 1px solid var(--rule); }
  .feature svg { width: 30px; height: 30px; fill: none; stroke: var(--white); stroke-width: 1.6; }
  .feature-label {
    font-family: "Open Sans", sans-serif; font-weight: 700;
    font-size: 6.6px; line-height: 1.35; color: var(--white);
    text-transform: uppercase; text-align: center;
  }

  .rollup-footer {
    flex: 1; position: relative;
    background: var(--ink);
  }
  .footer-photo {
    position: absolute; inset: 0 0 40px 0;
    background:
      radial-gradient(ellipse 60% 45% at 25% 8%, #9a78ae 0%, transparent 100%),
      radial-gradient(ellipse 40% 30% at 80% 20%, #6b5c9c 0%, transparent 100%),
      radial-gradient(ellipse 65% 45% at 60% 70%, #000 0%, transparent 100%),
      linear-gradient(180deg, #5a4f94 0%, #2e285c 35%, var(--ink) 80%);
  }
  .brand-name {
    position: absolute; left: 0; right: 0; bottom: 30px;
    font-family: "Bebas Neue", sans-serif; font-weight: 400;
    font-size: 34px; line-height: 1; color: var(--white); text-align: center; letter-spacing: 0.5px;
  }
</style>
</head>
<body>
  <main class="rollup">
    <header class="rollup-header">
      <h1 class="rollup-title">Advanced Combat Training Systems<br>for Realistic Combat Simulation</h1>
    </header>

    <div class="illustration illustration--field" role="img" aria-label="Isometric illustration of two battle tanks, three targets and an instructor truck with monitors and trainees"></div>

    <section class="feature-band">
      <div class="feature-grid">
        <div class="feature">
          <svg viewBox="0 0 26 26"><rect x="9" y="6" width="8" height="18" rx="2"/><circle cx="13" cy="11" r="2"/><path d="M11 16h4M11 19h4M9 3.5a6 6 0 0 1 8 0"/></svg>
          <p class="feature-label">Remote-control<br>functions</p>
        </div>
        <div class="feature">
          <svg viewBox="0 0 26 26"><path d="M4 5h18M5 5a8 8 0 0 0 16 0"/><circle cx="13" cy="10" r="2.5"/><path d="M13 18v4"/></svg>
          <p class="feature-label">16 camera systems<br>per vehicle</p>
        </div>
        <div class="feature">
          <svg viewBox="0 0 26 26"><rect x="3" y="8" width="20" height="14" rx="3"/><path d="M9 8l2-4h4l2 4"/><circle cx="13" cy="15" r="4.5"/><circle cx="13" cy="15" r="2"/></svg>
          <p class="feature-label">Optics<br>camera</p>
        </div>
        <div class="feature">
          <svg viewBox="0 0 26 26"><rect x="6" y="2" width="14" height="22" rx="2"/><path d="M9 7h8M9 11h8M9 15h8M9 19h5"/></svg>
          <p class="feature-label">Vehicle<br>data</p>
        </div>
        <div class="feature">
          <svg viewBox="0 0 26 26"><circle cx="11" cy="11" r="7"/><path d="M16 16l7 7"/></svg>
          <p class="feature-label">Full instructor<br>overview</p>
        </div>
        <div class="feature">
          <svg viewBox="0 0 26 26"><path d="M15 4a2.5 2.5 0 0 1 5 0v12a4 4 0 1 1-5 0z"/><path d="M11 8a5 5 0 0 0 0 10"/></svg>
          <p class="feature-label">Air-conditioned<br>instructor</p>
        </div>
        <div class="feature">
          <svg viewBox="0 0 26 26"><path d="M5 14a8 8 0 0 1 16 0"/><rect x="3" y="13" width="4" height="6" rx="1"/><rect x="19" y="13" width="4" height="6" rx="1"/><path d="M10 14v3M13 12v7M16 14v3M21 19q0 4-6 4"/></svg>
          <p class="feature-label">Full data<br>recording</p>
        </div>
        <div class="feature">
          <svg viewBox="0 0 26 26"><path d="M2 23L11 5l4 7 2-3 7 14z"/><path d="M13 15v5M10.5 17.5h5"/></svg>
          <p class="feature-label">All-weather &amp;<br>all-terrain</p>
        </div>
      </div>
    </section>

    <div class="illustration illustration--classroom" role="img" aria-label="Isometric illustration of a training room with trainees at desks facing two large wall screens"></div>

    <footer class="rollup-footer">
      <div class="footer-photo" role="img" aria-label="Photograph of a battle tank silhouetted against a dusk sky over grass"></div>
      <p class="brand-name">Bright Lantern Optics</p>
    </footer>
  </main>
</body>
</html>
```